BrivoPeak Business Card Design Project

We are looking for a modern, clean business card design for our new company. We are a consulting firm focused on the financial services market providing management and IT consulting to banks, insurance companies, etc. Please include our company logo and company contact information from the attached file in the design. Two versions of the logo are attached, either version is acceptable. Logos are available in other file formats if needed. We would like to include the contact information for both our UK and US offices as well as the following information for each individual card holder: Name, position/title, address, phone number and e-mail address.
Updates
Project Deadline Extended
Reason: A last minute trip over seas has prevented us from finalizing the decision. A decision will be made this week. We apologize for the inconvenience.
Industry/Entity Type
Business
Contact Information for Business Card
Company logo.
Company locations and phone numbers for both the US and UK offices.
Company URL.
Cardholder Name
Cardholder Position/title
Cardholder Address
Cardholder Phone Number
Cardholder e-mail Address
Look and feel
Each slider illustrates characteristics of the customer's brand and the style your logo design should communicate.

```html
<!DOCTYPE html>
<html lang="en">
<head>
<meta charset="utf-8">
<title>BrivoPeak Partners Business Card</title>
<link href="https://fonts.googleapis.com/css2?family=Open+Sans:wght@400;600;700&display=swap" rel="stylesheet">
<style>
  :root {
    --navy: #283c64;
    --grey: #6e6e70;
    --text-grey: #6a6a6c;
    --paper: #ffffff;
    --paper-shade: #f1f1f1;
    --backdrop: #e4e5e8;
  }
  * { box-sizing: border-box; margin: 0; padding: 0; }
  html, body { width: 1200px; height: 900px; overflow: hidden; }
  body {
    background: var(--backdrop);
    font-family: "Open Sans", Arial, sans-serif;
    position: relative;
  }
  .card {
    position: absolute;
    left: 290px;
    width: 620px;
    height: 354px;
    border-radius: 3px;
    box-shadow: 0 6px 18px rgba(0,0,0,0.18);
    overflow: hidden;
  }
  .card-back { top: 64px; background: var(--navy); }
  .card-front { top: 482px; background: linear-gradient(135deg, var(--paper) 40%, var(--paper-shade)); }

  .brand { display: flex; align-items: center; gap: 14px; }
  .brand-square { width: 34px; height: 34px; }
  .brand-name { font-weight: 700; line-height: 1; }

  .card-back .brand { position: absolute; left: 0; right: 0; top: 118px; justify-content: center; }
  .card-back .brand-square { background: #ffffff; }
  .card-back .brand-name { color: #ffffff; font-size: 44px; }
  .card-back .web { position: absolute; left: 0; right: 0; top: 230px; text-align: center; color: #ffffff; font-size: 15px; font-weight: 600; }

  .card-front .brand { position: absolute; left: 36px; top: 30px; }
  .card-front .brand-square { width: 30px; height: 30px; background: var(--grey); }
  .card-front .brand-name { color: var(--navy); font-size: 34px; }

  .holder { position: absolute; left: 36px; top: 92px; }
  .holder-name { color: var(--navy); font-size: 22px; font-weight: 400; line-height: 28px; }
  .holder-title { color: var(--text-grey); font-size: 13px; line-height: 18px; margin-bottom: 8px; }
  .contact-list { list-style: none; }
  .contact-list li { display: flex; align-items: center; gap: 8px; color: var(--text-grey); font-size: 14px; line-height: 21px; }
  .contact-list svg { width: 12px; height: 12px; fill: var(--navy); flex: none; }

  .offices { position: absolute; left: 350px; top: 128px; color: var(--text-grey); font-size: 14px; line-height: 18px; }
  .offices .company { color: var(--navy); font-weight: 600; font-size: 14px; }
  .offices address { font-style: normal; margin-bottom: 6px; }

  .wave { position: absolute; left: 0; bottom: 0; width: 620px; height: 110px; }
</style>
</head>
<body>

<section class="card card-back">
  <div class="brand">
    <span class="brand-square"></span>
    <span class="brand-name">BrivoPeak Partners</span>
  </div>
  <p class="web">www.brivopeakpartners.com</p>
</section>

<section class="card card-front">
  <svg class="wave" viewBox="0 0 620 110" preserveAspectRatio="none" aria-hidden="true">
    <path d="M0 4 C150 0 280 40 380 80 C450 104 540 106 620 98 L620 110 L0 110 Z" fill="var(--grey)"/>
    <path d="M0 12 C150 9 280 49 372 88 C440 112 540 114 620 108 L620 110 L0 110 Z" fill="var(--paper)"/>
    <path d="M0 16 C150 13 278 53 368 92 C436 116 540 118 620 112 L620 110 L0 110 Z" fill="var(--navy)"/>
  </svg>

  <div class="brand">
    <span class="brand-square"></span>
    <span class="brand-name">BrivoPeak Partners</span>
  </div>

  <div class="holder">
    <h1 class="holder-name">Daniel Whitmore</h1>
    <p class="holder-title">Manager</p>
    <ul class="contact-list">
      <li><svg viewBox="0 0 12 12"><path d="M2 1 L4.5 1 L5.3 3.5 L3.8 4.6 C4.5 6 6 7.5 7.4 8.2 L8.5 6.7 L11 7.5 L11 10 C11 10.6 10.6 11 10 11 C5 11 1 7 1 2 C1 1.4 1.4 1 2 1 Z"/></svg>(801) 555-0142 (US)</li>
      <li><svg viewBox="0 0 12 12"><path d="M2 1 L4.5 1 L5.3 3.5 L3.8 4.6 C4.5 6 6 7.5 7.4 8.2 L8.5 6.7 L11 7.5 L11 10 C11 10.6 10.6 11 10 11 C5 11 1 7 1 2 C1 1.4 1.4 1 2 1 Z"/></svg>+44 7700 900418 (UK)</li>
      <li><svg viewBox="0 0 12 12"><path d="M0 2 H12 V10 H0 Z M1 3 L6 6.5 L11 3 V3.2 L6 7.5 L1 3.2 Z" fill-rule="evenodd"/></svg>daniel@brivopeakpartners.com</li>
      <li><svg viewBox="0 0 12 12"><circle cx="6" cy="6" r="5.5"/><path d="M1 6 H11 M6 0.5 C3 3 3 9 6 11.5 C9 9 9 3 6 0.5" stroke="#fff" stroke-width="0.8" fill="none"/></svg>www.brivopeakpartners.com</li>
    </ul>
  </div>

  <div class="offices">
    <p class="company">BrivoPeak Partners</p>
    <address>418 N Maple Ave, Suite 210<br>Lindon UT 84042<br>United States</address>
    <address>14 Harrow Street<br>London EC2A 4QP<br>Great Britain</address>
  </div>
</section>

</body>
</html>
```